Business Card Design Project

Name: Kunle O. Edet
Designation: Partner
Address: QRM Building, 14 Harmony Close, P.O. Box 58314, Victoria Island Lagos, Nigeria
Tel: +234 1 7395162
mobile: +234 1 7061527394
Email: koedet@larkmoorassociates.com
website www.larkmoorassociates.com

```html
<!DOCTYPE html>
<html lang="en">
<head>
<meta charset="utf-8">
<title>Larkmoor Associates – Business Card</title>
<link rel="stylesheet" href="https://fonts.googleapis.com/css2?family=Source+Sans+3:wght@400;600&display=swap">
<style>
  :root {
    --backdrop: #e9e7e3;
    --card-dark: #1f1c1d;
    --card-dark-hi: #3a3637;
    --card-white: #ffffff;
    --ring-grey: #c4c4c4;
    --brand-grey: #8c8c8c;
    --brand-silver: #cfcfcf;
    --text-light: #f2f2f2;
    --text-muted: #cfcfcf;
  }
  html, body {
    margin: 0;
    padding: 0;
    width: 1200px;
    height: 902px;
    overflow: hidden;
    background: var(--backdrop);
    font-family: "Source Sans 3", "Myriad Pro", sans-serif;
  }
  .canvas {
    position: relative;
    width: 1200px;
    height: 902px;
  }
  .card {
    position: absolute;
    width: 520px;
    height: 297px;
    overflow: hidden;
    border-radius: 3px;
    box-shadow: 0 6px 18px rgba(0,0,0,0.22);
    background: linear-gradient(135deg, var(--card-dark) 0%, var(--card-dark-hi) 55%, var(--card-dark) 100%);
  }
  .card--front { left: 60px; top: 150px; }
  .card--back  { left: 620px; top: 455px; }

  /* Front */
  .front-brand {
    position: absolute;
    left: 150px;
    top: 110px;
    display: flex;
    align-items: center;
    gap: 16px;
    color: var(--brand-silver);
    font-weight: 400;
  }
  .brand-square {
    width: 40px;
    height: 40px;
    background: var(--brand-silver);
  }
  .brand-name { line-height: 1; }
  .brand-name__main { display: block; font-size: 44px; letter-spacing: 0.5px; }
  .brand-name__sub { display: block; font-size: 20px; text-align: right; margin-top: 2px; }

  /* Back */
  .back-arc {
    position: absolute;
    inset: 0;
  }
  .back-brand {
    position: absolute;
    left: 24px;
    top: 185px;
    display: flex;
    align-items: center;
    gap: 12px;
    color: var(--brand-grey);
    font-weight: 400;
  }
  .back-brand .brand-square {
    width: 30px;
    height: 30px;
    background: var(--brand-grey);
  }
  .back-brand .brand-name__main { font-size: 34px; }
  .back-brand .brand-name__sub { font-size: 16px; }

  .contact {
    position: absolute;
    right: 24px;
    top: 22px;
    text-align: right;
    color: var(--text-light);
  }
  .contact__name {
    margin: 0;
    font-size: 17px;
    font-weight: 600;
    line-height: 1.1;
  }
  .contact__role {
    margin: 2px 0 0;
    font-size: 10px;
    color: var(--text-muted);
  }
  .contact__details {
    margin: 44px 0 0;
    padding: 0;
    list-style: none;
    font-size: 12px;
    line-height: 1.55;
  }
</style>
</head>
<body>
<main class="canvas">

  <section class="card card--front" aria-label="Business card front">
    <div class="front-brand">
      <span class="brand-square" aria-hidden="true"></span>
      <span class="brand-name">
        <span class="brand-name__main">Larkmoor</span>
        <span class="brand-name__sub">Associates</span>
      </span>
    </div>
  </section>

  <section class="card card--back" aria-label="Business card back">
    <svg class="back-arc" width="520" height="297" viewBox="0 0 520 297" aria-hidden="true">
      <circle cx="0" cy="330" r="284" fill="var(--ring-grey)"/>
      <circle cx="0" cy="330" r="270" fill="var(--card-white)"/>
    </svg>

    <div class="back-brand">
      <span class="brand-square" aria-hidden="true"></span>
      <span class="brand-name">
        <span class="brand-name__main">Larkmoor</span>
        <span class="brand-name__sub">Associates</span>
      </span>
    </div>

    <div class="contact">
      <p class="contact__name">Kunle O. Edet</p>
      <p class="contact__role">Designation: Partner</p>
      <ul class="contact__details">
        <li>Tel: +234 1 7395162</li>
        <li>mobile: +234 1 7061527394</li>
        <li>Email: koedet@larkmoorassociates.com</li>
        <li>website www.larkmoorassociates.com</li>
        <li>Address: QRM Building, 14 Harmony Close,</li>
        <li>P.O. Box 58314, Victoria Island Lagos, Nigeria</li>
      </ul>
    </div>
  </section>

</main>
</body>
</html>
```